Korvane Development and Management Corp. Business Card

A logo design project has been started for our Calgary-Alberta, Canada based land development and project management company. Using this logo, a clean, sleek, professional business card is to be developed (for digital or print media) representing the principals of the company (community, sustainability, and harmony).
Updates

Reason: Logo design recently completed.

Adobe Illustrator Vector file uploaded. Thanks, Lev

Target Market(s)

Similar business development professionals and other engineering project management personnel involved in land developemtn. Also used to as as the brand and image with both private individuals (Landowners), public officials (policy makers), and investors (banks, venture capitalists).

Industry/Entity Type

Digital

Requirements
Must have
• Open to designers opinion. Based on logo. Must have logo, and space for employee name, title, address, website, office / cell numbers.
Should not have
• No Palm trees or tropical references. Company is based in Calgary, Alberta, Canada.

```html
<!DOCTYPE html>
<html lang="en">
<head>
<meta charset="utf-8">
<title>Korvane Development and Management Corp. Business Card</title>
<link href="https://fonts.googleapis.com/css2?family=Cinzel:wght@400;600&family=Cormorant+Garamond:wght@500&display=swap" rel="stylesheet">
<style>
  :root {
    --backdrop: #e9e6e0;
    --card-light: #ffffff;
    --card-shade: #e6e7e8;
    --leaf: #8cb832;
    --leaf-deep: #6f9a1f;
    --slate: #7d8288;
    --slate-light: #b9bcc0;
    --ink: #6a6e73;
  }
  * { box-sizing: border-box; margin: 0; padding: 0; }
  html, body {
    width: 1200px; height: 600px; overflow: hidden;
    background: var(--backdrop);
  }
  .business-card {
    position: absolute; left: 180px; top: 60px;
    width: 840px; height: 480px;
    border-radius: 22px; overflow: hidden;
    background: radial-gradient(ellipse at 30% 35%, var(--card-light) 0%, var(--card-shade) 100%);
    box-shadow: 0 10px 30px rgba(0,0,0,.18);
  }
  .swoosh { position: absolute; inset: 0; width: 100%; height: 100%; }

  .brand { position: absolute; left: 70px; top: 136px; }
  .brand-name {
    display: flex; align-items: center; gap: 16px;
    font-family: "Cinzel", serif; font-weight: 600;
    font-size: 72px; line-height: 1; letter-spacing: 3px;
    color: var(--leaf);
  }
  .brand-mark { width: 32px; height: 32px; background: var(--slate); }
  .brand-tagline {
    margin: 8px 0 0 50px;
    font-family: "Cormorant Garamond", serif; font-weight: 500;
    font-size: 22px; color: var(--ink);
  }
  .divider {
    position: absolute; left: 70px; top: 282px;
    width: 440px; height: 2px; background: var(--leaf);
  }
  .contacts {
    position: absolute; left: 70px; top: 306px;
    list-style: none;
    font-family: "Cinzel", serif; font-size: 17px; color: var(--ink);
  }
  .contacts li { display: flex; align-items: center; gap: 12px; height: 30px; }
  .contact-icon { width: 18px; height: 18px; flex: none; }

  .person { position: absolute; right: 60px; top: 60px; text-align: right; }
  .person-name {
    font-family: "Cinzel", serif; font-weight: 600;
    font-size: 30px; color: var(--leaf); letter-spacing: 1px;
  }
  .person-title {
    font-family: "Cinzel", serif; font-size: 18px; color: var(--ink);
    margin-top: 2px;
  }
  .person-rule { width: 230px; height: 2px; background: var(--leaf); margin: 14px 0 14px auto; }
  .person-address {
    font-family: "Cinzel", serif; font-size: 17px; line-height: 1.5; color: var(--ink);
  }
</style>
</head>
<body>
  <article class="business-card">
    <svg class="swoosh" viewBox="0 0 840 480" preserveAspectRatio="none" aria-hidden="true">
      <path d="M300 480 C 520 470, 660 400, 730 330 C 775 285, 808 262, 840 250 L 840 480 Z" fill="var(--slate-light)"/>
      <path d="M340 480 C 545 466, 670 405, 740 338 C 782 296, 812 276, 840 268 L 840 480 Z" fill="var(--slate)"/>
      <path d="M420 480 C 595 462, 690 410, 752 350 C 790 312, 815 296, 840 290 L 840 480 Z" fill="var(--leaf)"/>
      <path d="M560 480 C 685 452, 755 400, 795 360 C 815 340, 828 330, 840 326 L 840 480 Z" fill="var(--leaf-deep)" opacity=".35"/>
    </svg>

    <header class="brand">
      <div class="brand-name"><span class="brand-mark"></span>KORVANE</div>
      <p class="brand-tagline">Development and Management Corp</p>
    </header>

    <div class="divider"></div>

    <ul class="contacts">
      <li>
        <svg class="contact-icon" viewBox="0 0 18 18"><rect width="18" height="18" rx="3" fill="var(--leaf)"/><path d="M5 4h3l1 3-2 1a7 7 0 0 0 3 3l1-2 3 1v3c-6 0-9-3-9-9z" fill="#fff"/></svg>
        +1 403 555 0142
      </li>
      <li>
        <svg class="contact-icon" viewBox="0 0 18 18"><rect width="18" height="18" rx="3" fill="var(--leaf)"/><rect x="6" y="3" width="6" height="12" rx="1" fill="#fff"/><rect x="7" y="5" width="4" height="7" fill="var(--leaf)"/></svg>
        +1 403 555 0187
      </li>
      <li>
        <svg class="contact-icon" viewBox="0 0 18 18"><rect width="18" height="18" rx="3" fill="var(--leaf)"/><rect x="3" y="5" width="12" height="8" fill="#fff"/><path d="M3 5l6 5 6-5" stroke="var(--leaf)" stroke-width="1.2" fill="none"/></svg>
        info@korvane.com
      </li>
      <li>
        <svg class="contact-icon" viewBox="0 0 18 18"><rect width="18" height="18" rx="3" fill="var(--leaf)"/><circle cx="9" cy="9" r="5" fill="none" stroke="#fff" stroke-width="1.4"/><path d="M4 9h10M9 4c-2.5 3-2.5 7 0 10M9 4c2.5 3 2.5 7 0 10" stroke="#fff" stroke-width="1" fill="none"/></svg>
        www.korvane.com
      </li>
    </ul>

    <section class="person">
      <h2 class="person-name">Mara Ellison</h2>
      <p class="person-title">Founder &amp; CEO</p>
      <div class="person-rule"></div>
      <p class="person-address">Here your company or<br>home address</p>
    </section>
  </article>
</body>
</html>
```